NGO VOILES DE LUMA CAR COVERING

Hello, our NGO needs its covering.
Here are our wishes:
The vehicle is a white 2022 KOLVEN BARTEX DUO K3P2 with side windows at passengers side. The rear door is a double door.
Our NGO: we care about orphans and provide clear water to populations in Africa.
What must appear:
Our logo (hexa-color logo):
Brown: #8B5D3C (RGB: 139 93 60)
Green: #39B54A (RGB: 57 181 74)
Our motto: "An association that reflects you and unites us"
Phone number: 01 47 26 38 59
Add pikoria, lumagraph and zumzum logo
As well as our site www.voilesdelumarive.com

Surprise us!!

No need of real photos on the project, just what is expressed on it. All scriptures must be in French.

```html
<!DOCTYPE html>
<html lang="fr">
<head>
<meta charset="utf-8">
<title>Voiles de Luma – habillage véhicule</title>
<link rel="stylesheet" href="https://fonts.googleapis.com/css2?family=Cinzel:wght@400;600&display=swap">
<style>
  :root{
    --green:#39b54a;
    --brown:#8b5d3c;
    --white:#ffffff;
    --body-white:#f4f5f5;
    --glass:#2b2d2f;
    --glass-light:#8e9194;
    --trim:#1d1e20;
    --tyre:#222325;
    --hub:#b9bcbf;
    --lamp-red:#b3121a;
    --lamp-grey:#c9cbcd;
    --bg:#ffffff;
  }
  html,body{margin:0;padding:0;width:1200px;height:1200px;overflow:hidden;background:var(--bg);}
  .wrap-sheet{display:block;width:1200px;height:1200px;}
  .brand-text{font-family:"Cinzel",serif;}
  .name{fill:var(--brown);font-weight:400;}
  .motto{fill:var(--white);font-weight:400;}
  .phone-side{fill:var(--green);stroke:var(--white);stroke-width:3;paint-order:stroke;font-weight:600;}
  .phone{fill:var(--green);font-weight:400;}
  .site{fill:var(--brown);font-weight:400;}
</style>
</head>
<body>
<svg class="wrap-sheet" viewBox="0 0 1920 1920" xmlns="http://www.w3.org/2000/svg">

  <!-- ===== SIDE VIEW ===== -->
  <g class="van-side">
    <path class="body" d="M140,700 L138,600 Q150,520 240,440 L460,320 L800,182 L1750,163 Q1790,168 1795,230 L1800,640 L1800,670 L140,700 Z" fill="var(--body-white)"/>
    <path class="wrap-green" d="M432,378 L800,182 L1750,163 Q1790,168 1795,230 L1797,528 C1640,532 1450,552 1340,572 L560,590 Z" fill="var(--green)"/>
    <path class="wrap-band" d="M560,590 L1340,572 C1450,552 1640,532 1797,528 L1797,548 C1640,552 1460,570 1340,592 L548,604 Z" fill="var(--brown)"/>
    <path class="cab-window" d="M470,380 L520,300 Q600,230 660,212 L810,208 Q822,212 818,240 L800,380 L520,412 Z" fill="var(--glass)"/>
    <rect class="side-window" x="888" y="198" width="812" height="190" rx="26" fill="var(--glass)"/>
    <rect x="922" y="235" width="360" height="130" rx="10" fill="var(--glass-light)" opacity=".55"/>
    <rect x="1295" y="222" width="370" height="140" rx="10" fill="var(--glass-light)" opacity=".55"/>
    <path class="rear-lamp" d="M1765,300 L1788,300 L1790,450 L1765,450 Z" fill="var(--lamp-red)"/>
    <path class="sill" d="M140,650 L1800,636 L1802,670 L140,700 Z" fill="var(--trim)"/>
    <circle cx="395" cy="690" r="100" fill="var(--tyre)"/>
    <circle cx="395" cy="690" r="62" fill="var(--hub)"/>

    <circle class="logo-mark" cx="640" cy="505" r="82" fill="none" stroke="var(--brown)" stroke-width="7"/>
    <text class="brand-text name" x="662" y="635" font-size="31" text-anchor="middle" letter-spacing="1">VOILES DE LUMA</text>

    <text class="brand-text motto" x="1098" y="440" font-size="35" text-anchor="middle">UNE ASSOCIATION</text>
    <text class="brand-text motto" x="1098" y="480" font-size="35" text-anchor="middle">QUI VOUS RESSEMBLE</text>
    <text class="brand-text motto" x="1098" y="520" font-size="35" text-anchor="middle">ET NOUS RASSEMBLE</text>
    <text class="brand-text phone-side" x="1102" y="588" font-size="62" text-anchor="middle">01 47 26 38 59</text>
    <text class="brand-text site" x="1104" y="622" font-size="25" text-anchor="middle">WWW.VOILESDELUMARIVE.COM</text>

    <circle class="deco-ring" cx="1505" cy="505" r="158" fill="var(--body-white)" stroke="var(--brown)" stroke-width="10"/>
    <circle cx="1520" cy="690" r="100" fill="var(--tyre)"/>
    <circle cx="1520" cy="690" r="62" fill="var(--hub)"/>
  </g>

  <!-- ===== REAR VIEW ===== -->
  <g class="van-rear">
    <path class="body" d="M130,980 Q132,960 170,958 L840,955 Q876,958 880,990 L905,1610 L105,1610 Z" fill="var(--green)"/>
    <path class="wrap-white" d="M105,1480 C300,1510 500,1490 905,1425 L905,1610 L105,1610 Z" fill="var(--body-white)"/>
    <path class="wrap-band" d="M105,1465 C300,1495 500,1475 905,1410 L905,1428 C500,1495 300,1515 105,1486 Z" fill="var(--brown)"/>
    <rect class="rear-window" x="205" y="1000" width="600" height="278" rx="24" fill="var(--glass)"/>
    <line x1="507" y1="955" x2="507" y2="1610" stroke="var(--trim)" stroke-width="3"/>
    <rect x="108" y="1135" width="52" height="215" rx="6" fill="var(--lamp-red)"/>
    <rect x="850" y="1135" width="52" height="215" rx="6" fill="var(--lamp-red)"/>
    <rect x="118" y="1440" width="38" height="75" rx="4" fill="var(--lamp-grey)"/>
    <rect x="852" y="1440" width="38" height="75" rx="4" fill="var(--lamp-grey)"/>

    <circle class="logo-mark" cx="357" cy="1113" r="50" fill="none" stroke="var(--brown)" stroke-width="5"/>
    <text class="brand-text name" x="357" y="1197" font-size="27" text-anchor="middle">VOILES DE LUMA</text>

    <circle class="deco-ring" cx="333" cy="1425" r="130" fill="var(--body-white)" stroke="var(--brown)" stroke-width="9"/>
    <rect class="plate" x="222" y="1515" width="228" height="46" rx="4" fill="var(--white)" stroke="#d6d6d6"/>

    <text class="brand-text motto" x="520" y="1360" font-size="26">UNE ASSOCIATION</text>
    <text class="brand-text motto" x="520" y="1393" font-size="26">QUI VOUS RESSEMBLE</text>
    <text class="brand-text motto" x="520" y="1426" font-size="26">ET NOUS RASSEMBLE</text>
    <text class="brand-text phone" x="522" y="1562" font-size="44">01 47 26 38 59</text>
    <text class="brand-text site" x="522" y="1590" font-size="19">WWW.VOILESDELUMARIVE.COM</text>

    <rect class="bumper" x="112" y="1610" width="786" height="55" rx="10" fill="var(--trim)"/>
    <rect x="128" y="1665" width="105" height="110" rx="18" fill="var(--tyre)"/>
    <rect x="778" y="1665" width="105" height="110" rx="18" fill="var(--tyre)"/>
  </g>

  <!-- ===== FRONT VIEW ===== -->
  <g class="van-front">
    <path class="body" d="M1085,1010 Q1090,1000 1120,998 L1660,998 Q1690,1000 1695,1010 L1785,1400 L1785,1640 L995,1640 L995,1400 Z" fill="var(--body-white)"/>
    <path class="windshield" d="M1095,1020 L1690,1020 L1728,1210 L1052,1210 Z" fill="var(--glass)"/>
    <rect x="948" y="1162" width="70" height="88" rx="14" fill="var(--trim)"/>
    <rect x="1762" y="1162" width="70" height="88" rx="14" fill="var(--trim)"/>

    <circle class="logo-mark" cx="1387" cy="1250" r="29" fill="none" stroke="var(--brown)" stroke-width="5"/>
    <text class="brand-text name" x="1387" y="1318" font-size="28" text-anchor="middle" letter-spacing="3">VOILES DE LUMA</text>

    <path class="headlamp" d="M1010,1300 L1140,1340 L1130,1400 L1012,1380 Z" fill="var(--glass-light)"/>
    <path class="headlamp" d="M1770,1300 L1640,1340 L1650,1400 L1768,1380 Z" fill="var(--glass-light)"/>
    <path class="grille" d="M1140,1340 L1640,1340 L1605,1500 L1175,1500 Z" fill="var(--trim)"/>
    <line x1="1150" y1="1370" x2="1630" y2="1370" stroke="var(--hub)" stroke-width="5"/>
    <line x1="1160" y1="1415" x2="1620" y2="1415" stroke="var(--hub)" stroke-width="5"/>
    <line x1="1170" y1="1460" x2="1610" y2="1460" stroke="var(--hub)" stroke-width="5"/>
    <path class="bumper" d="M998,1520 L1785,1520 L1778,1660 Q1770,1690 1740,1690 L1040,1690 Q1010,1690 1002,1660 Z" fill="var(--trim)"/>
    <rect class="plate" x="1318" y="1548" width="140" height="36" rx="4" fill="var(--white)"/>
    <rect x="1008" y="1690" width="92" height="70" rx="16" fill="var(--tyre)"/>
    <rect x="1680" y="1690" width="92" height="70" rx="16" fill="var(--tyre)"/>
  </g>
</svg>
</body>
</html>
```